Vital Spark Electrical in need of a business card design

We need a new business card designed for our electrical business. We have a logo already which I will attach below.
Would like the business card to be..
-BLACK background preferably, possibly white back ground behind logo if colours clash.
-White & Blue (logo blue) text
Something that makes the logo pop, & a modern look. Possibly minimal clean format.

REQUIRE:
-Logo on front & back

TEXT TO INCLUDE (ON ONE SIDE):

Tom Harlow
Director/Electrician
M: 0417 365 208
E:info@vitalsparkelectrical-example.com.au
W:www.vitalsparkelectrical-example.com.au
R.E.C 57318

Custom/New Homes
Renovations
Commercial Office/Shop Fit-outs
Communications & Security Cameras
Electric Vehicle Chargers
Airconditioning
Updates

Requirements
Nice to have
• Possibly even lighten the grey shades for the words 'Vital' & 'Spark' to be more easily read on a black background.

```html
<!DOCTYPE html>
<html lang="en">
<head>
<meta charset="utf-8">
<title>Vital Spark Electrical – Business Card</title>
<link rel="stylesheet" href="https://fonts.googleapis.com/css2?family=Montserrat:wght@400;500;600&display=swap">
<style>
  :root {
    --blue: #0aa0e0;
    --slate: #313c47;
    --ink: #3a4550;
    --grey-text: #4a5560;
    --white: #ffffff;
    --backdrop: #e6e6e6;
  }
  * { margin: 0; padding: 0; box-sizing: border-box; }
  html, body {
    width: 1200px; height: 1028px; overflow: hidden;
    background: var(--backdrop);
    font-family: "Montserrat", sans-serif;
  }
  .card {
    position: absolute; left: 310px; width: 579px; height: 331px;
    border-radius: 18px; overflow: hidden;
  }
  .card--front { top: 165px; background: var(--white); }
  .card--back { top: 532px; background: var(--slate); }

  .brand { position: absolute; display: flex; align-items: center; font-weight: 600; white-space: nowrap; }
  .brand__square { background: var(--blue); flex: none; }
  .card--front .brand { left: 34px; top: 40px; gap: 10px; font-size: 21px; color: var(--ink); }
  .card--front .brand__square { width: 16px; height: 16px; }
  .card--back .brand { left: 0; right: 0; top: 96px; justify-content: center; gap: 14px; font-size: 30px; color: var(--white); }
  .card--back .brand__square { width: 26px; height: 26px; }

  .accent-bar { position: absolute; top: 151px; height: 45px; }
  .accent-bar--blue { left: 0; width: 8px; background: var(--blue); }
  .accent-bar--slate { left: 11px; width: 2.5px; background: var(--slate); }

  .person { position: absolute; left: 34px; top: 151px; }
  .person__name { font-size: 25px; font-weight: 500; color: var(--blue); letter-spacing: 0.5px; line-height: 1.1; text-transform: uppercase; }
  .person__role { font-size: 14px; color: var(--grey-text); margin-top: 4px; }

  .services {
    position: absolute; left: 270px; width: 282px; top: 114px;
    list-style: none; text-align: center;
    font-size: 14px; line-height: 20px; color: var(--ink);
  }

  .contacts { position: absolute; left: 34px; top: 241px; list-style: none; font-size: 14px; color: var(--grey-text); }
  .contacts li { display: flex; align-items: center; gap: 8px; height: 20px; }
  .contacts svg { width: 12px; height: 12px; flex: none; }

  .footer-band { position: absolute; left: 0; bottom: 0; width: 579px; height: 331px; }
  .licence { position: absolute; right: 30px; top: 304px; font-size: 14px; color: var(--white); }
  .licence__label { color: var(--blue); }

  .back-url {
    position: absolute; left: 0; right: 0; top: 283px; text-align: center;
    font-size: 13px; letter-spacing: 3px; color: var(--white);
  }
</style>
</head>
<body>

<section class="card card--front" aria-label="Front of card">
  <div class="brand"><span class="brand__square"></span>Vital Spark Electrical</div>

  <span class="accent-bar accent-bar--blue"></span>
  <span class="accent-bar accent-bar--slate"></span>

  <div class="person">
    <p class="person__name">Tom Harlow</p>
    <p class="person__role">Director/Electrician</p>
  </div>

  <ul class="services">
    <li>Renovations</li>
    <li>Custom/New Homes</li>
    <li>Commercial Office/Shop Fit-outs</li>
    <li>Communications &amp; Security Cameras</li>
    <li>Electric Vehicle Chargers</li>
    <li>Airconditioning</li>
  </ul>

  <ul class="contacts">
    <li>
      <svg viewBox="0 0 12 12" aria-hidden="true"><path d="M2.5 1 L4.5 1 L5 3.5 L3.8 4.4 C4.4 5.8 5.5 7 7 7.8 L8 6.8 L10.5 7.3 L10.5 9.5 C10.5 10.2 10 10.8 9.2 10.7 C5 10.2 1.6 6.8 1.2 2.6 C1.1 1.7 1.7 1 2.5 1 Z" fill="none" stroke="var(--blue)" stroke-width="1.1"/></svg>
      0417 365 208
    </li>
    <li>
      <svg viewBox="0 0 12 12" aria-hidden="true"><rect x="1" y="2.5" width="10" height="7" fill="none" stroke="var(--blue)" stroke-width="1.1"/><path d="M1 2.5 L6 6.5 L11 2.5" fill="none" stroke="var(--blue)" stroke-width="1.1"/></svg>
      info@vitalsparkelectrical-example.com.au
    </li>
    <li>
      <svg viewBox="0 0 12 12" aria-hidden="true"><g fill="none" stroke="var(--blue)" stroke-width="1"><circle cx="6" cy="6" r="5"/><ellipse cx="6" cy="6" rx="2.2" ry="5"/><path d="M1 6 H11 M1.8 3.5 H10.2 M1.8 8.5 H10.2"/></g></svg>
      www.vitalsparkelectrical-example.com.au
    </li>
  </ul>

  <svg class="footer-band" viewBox="0 0 579 331" aria-hidden="true">
    <path d="M0 320 L330 320 C348 320 356 305 378 305 L579 305 L579 331 L0 331 Z" fill="var(--slate)"/>
    <path d="M2 313 L332 313 C338 313 342 311 346 309" fill="none" stroke="var(--blue)" stroke-width="4"/>
  </svg>
  <p class="licence"><span class="licence__label">R.E.C</span> 57318</p>
</section>

<section class="card card--back" aria-label="Back of card">
  <div class="brand"><span class="brand__square"></span>Vital Spark Electrical</div>
  <p class="back-url">www.vitalsparkelectrical-example.com.au</p>
</section>

</body>
</html>
```